New webpage for Facility Management Company (cleaning services)

We need a new web page design for a company based in Stockholm, Sweden, called TKR Clean AB (established 1991). We provide cleaning services to the public sector, to businesses, and to home owners. Our services primarily include daily cleaning, floor care, window cleaning, and carpet cleaning.

Our company holds certificates for ISO 9001, ISO 14001, ISO 45001 and "Hjorten".

Referring to "the Swedish model" we honor collective agreements between Veltrio (employer-representative organisation and relevant labour unions (e.g. Arbetsfront).
The final design should communicate that we are a trustworthy company with a well trained staff, high quality services combined with a commitment to run a sustainable business from a labour and environmental perspective.

DETAILS
General
-----------------------------------------------
• Language: Swedish (we provide text)
• Very important: Easy to administrate for company staff without special technical skills, especially to
o add/change information about HQ staff
o change any text
o add/change information about offered services
• Responsive
• SEO-friendly

Content that web page needs to cover in one way or the other
--------------------------------------------
• Information about our company
• About our staff and contact info to HQstaff/management (photos, contact info)
• Our ambitions and supporting info (quality, environment, labour conditions, certificates, etc)
• Information to customers within the public sector
• Information to customers within the private sector
• Information to customers within the home owner sector
• Services public sector (Swedish = Offentlig sektor)
• Services private business sector (Swedish = Företag) Se törnvall
• Services home owner sector (Swedish=Privat)
• GDPR compliance
• News

Content/Function
-------------------------------
• One specific requirement is that we need a page for information to potentially new employees (some general information and open job positions) with a possibility to fill in a simple application form and upload CV.(Mail?) CAPTCHA or equivalent.
• Contact form for customers with CAPTCHA or equivalent.
• Cookie management
• Integration social media (future); easy to manage/add/delete integration of social media.

We are not interested in a blog at this point of time

```html
<!DOCTYPE html>
<html lang="en">
<head>
<meta charset="utf-8">
<title>TKR Clean AB – Cleaning Services</title>
<link href="https://fonts.googleapis.com/css2?family=Poppins:ital,wght@0,300;0,400;0,500;0,600;0,700;0,800;1,400&display=swap" rel="stylesheet">
<style>
:root{
  --green:#6ab23e;
  --green-dark:#58a02e;
  --blue:#1a8fd6;
  --ink:#111111;
  --text:#333333;
  --muted:#555555;
  --light:#f4f5f7;
  --footer:#121212;
  --white:#ffffff;
}
*{margin:0;padding:0;box-sizing:border-box}
html,body{width:1200px;height:4367px;overflow:hidden;background:var(--white)}
body{font-family:'Poppins',sans-serif;color:var(--text)}
.page{position:relative;width:1200px;height:4367px;overflow:hidden}
.abs{position:absolute}
.eyebrow{position:absolute;font-size:13px;font-weight:500;letter-spacing:3.5px;color:var(--blue)}
.center{left:0;width:1200px;text-align:center}
.h2{position:absolute;font-size:40px;line-height:1.12;color:var(--ink);font-weight:300}
.h2 b{font-weight:700}
.lead{position:absolute;font-size:14px;line-height:21px;color:var(--muted)}
.btn{position:absolute;display:flex;align-items:center;justify-content:center;background:var(--green);color:var(--white);border-radius:20px;font-weight:500;box-shadow:0 4px 10px rgba(0,0,0,.15)}
.photo{position:absolute;overflow:hidden}

/* header */
.logo{position:absolute;display:flex;align-items:center;gap:6px;font-weight:500;color:var(--ink)}
.logo i{display:block;border-radius:50%;background:var(--green)}
.nav{position:absolute;top:22px;left:440px;display:flex;gap:0;font-size:15px;font-weight:500;color:var(--ink)}
.nav span{position:absolute;white-space:nowrap}

/* hero */
.hero-photo{left:0;top:0;width:1200px;height:619px;background:linear-gradient(90deg,#f6f6fb 0%,#efeff7 38%,#d8d8e0 55%,#b8b6b4 72%,#d9d2c9 100%)}
.hero-badge{position:absolute;left:88px;top:203px;height:20px;padding:0 10px;background:var(--blue);color:var(--white);font-size:12px;font-weight:600;letter-spacing:2.5px;line-height:20px;border-radius:2px}
.hero-title{position:absolute;left:86px;top:230px;font-size:70px;line-height:74px;color:var(--ink);font-weight:300;letter-spacing:-.5px}
.hero-title b{font-weight:800}

/* services */
.card{position:absolute;background:var(--white);border-radius:6px;box-shadow:0 4px 18px rgba(0,0,0,.10);overflow:hidden;text-align:center}
.card .img{height:195px}
.card h3{font-size:24px;line-height:26px;font-weight:600;color:var(--ink);margin-top:16px}
.card p{font-size:14px;line-height:21px;color:var(--muted);margin:14px 26px 0}
.card .more{display:flex;align-items:center;justify-content:center;gap:8px;font-size:14px;color:var(--ink);margin-top:18px}
.card.active{background:var(--green)}
.card.active h3,.card.active p,.card.active .more{color:var(--white)}
.dot{position:absolute;width:14px;height:14px;border-radius:50%;background:#a9d58d}
.dot.on{width:22px;height:22px;background:var(--green);border:4px solid #cfe6bf}

/* stats */
.stats{left:0;top:1925px;width:1200px;height:223px;background:linear-gradient(90deg,#2b2315 0%,#1a150d 35%,#0d0b08 60%,#3a2a17 100%)}
.stat{position:absolute;top:1988px;width:220px;text-align:center;color:var(--white)}
.stat strong{display:block;font-size:50px;line-height:56px;font-weight:700}
.stat span{display:block;font-size:19px;font-weight:600;margin-top:2px}

/* team */
.member{position:absolute;top:2368px;width:232px;height:291px;border-radius:8px;overflow:hidden;box-shadow:0 4px 14px rgba(0,0,0,.14)}
.member .tag{position:absolute;left:0;bottom:0;width:100%;height:56px;background:var(--green);color:var(--white);padding:10px 16px}
.member .tag b{display:block;font-size:15px;font-weight:600;line-height:18px}
.member .tag small{font-size:10px}
.member .soc{position:absolute;right:16px;bottom:18px;display:flex;gap:8px}
.member .soc i{width:10px;height:10px;border-radius:50%;background:var(--white);display:block}

/* testimonial */
.testi{left:0;top:2749px;width:1200px;height:471px;background:linear-gradient(90deg,#e8e8e8 0%,#f1f1f1 40%,#f7f7f7 100%)}
.arrow-btn{position:absolute;width:36px;height:36px;border-radius:50%;background:var(--white);box-shadow:0 2px 8px rgba(0,0,0,.2);display:flex;align-items:center;justify-content:center}

/* blog */
.post{position:absolute;top:3426px;width:281px;height:400px;background:var(--white);box-shadow:0 4px 16px rgba(0,0,0,.10);border-bottom:5px solid var(--green);text-align:center}
.post .img{height:187px;position:relative}
.post .date{position:absolute;right:16px;top:16px;width:34px;background:var(--green);color:var(--white);font-size:13px;line-height:17px;text-align:center;padding:4px 0;border-radius:3px}
.post .date hr{border:0;border-top:1px solid rgba(255,255,255,.7);margin:3px 0}
.post h4{font-size:19px;line-height:22px;font-weight:600;color:var(--ink);margin-top:32px}
.post p{font-size:12.5px;line-height:20px;color:var(--muted);margin:12px 30px 0}
.post .meta{position:absolute;left:18px;right:18px;bottom:16px;display:flex;align-items:center;gap:10px;font-size:11px;color:var(--muted)}
.post .meta i{width:28px;height:28px;border-radius:50%;background:#c9c9c9;border:2px solid #ddd;display:block}

/* newsletter + footer */
.footer{left:0;top:4009px;width:1200px;height:358px;background:var(--footer)}
.newsletter{left:92px;top:3919px;width:1016px;height:118px;background:var(--green);border-radius:12px;box-shadow:0 6px 14px rgba(0,0,0,.2)}
.fcol{position:absolute;top:4126px;color:var(--white);font-size:14px}
.fcol h5{font-size:16px;font-weight:400;margin-bottom:14px}
.fcol li{list-style:none;line-height:31px}
</style>
</head>
<body>
<div class="page">

  <!-- HERO -->
  <div class="photo hero-photo" role="img" aria-label="Smiling cleaner in blue overalls wiping a desk in a bright office"></div>
  <div class="logo" style="left:88px;top:28px;font-size:16px"><i style="width:18px;height:18px"></i>TKR Clean AB</div>
  <nav class="nav">
    <span style="left:2px">Home</span>
    <span style="left:90px;color:#444">|</span>
    <span style="left:139px">About us</span>
    <span style="left:252px;color:#444">|</span>
    <span style="left:299px">Services</span>
    <span style="left:408px;color:#444">|</span>
    <span style="left:454px">Pricing</span>
  </nav>
  <div class="btn" style="left:990px;top:17px;width:120px;height:39px;font-size:14px;border-radius:8px">Get Quate</div>

  <div class="hero-badge">Wellcome To TKR Clean AB</div>
  <h1 class="hero-title"><b>We</b> Provide<br>Cleaning <b>Services</b></h1>
  <p class="lead" style="left:88px;top:390px;width:540px;font-size:14px;color:#333">Lorem ipsum dolor sit amet, consectetur adipiscing elit, sed do eiusmod tempor incididunt ut.</p>
  <div class="btn" style="left:88px;top:451px;width:132px;height:39px;font-size:15px">Contact Us</div>

  <!-- ABOUT -->
  <div class="abs" style="left:208px;top:707px;width:326px;height:400px;background:var(--green)"></div>
  <div class="photo" role="img" aria-label="Cleaner in red apron holding a broom and a bucket of supplies" style="left:220px;top:720px;width:395px;height:394px;background:linear-gradient(135deg,#e6e6e6,#b9b9b9 55%,#8c8c8c);border-radius:6px;box-shadow:0 6px 16px rgba(0,0,0,.25)"></div>
  <div class="eyebrow" style="left:590px;top:840px">About us</div>
  <h2 class="h2" style="left:590px;top:856px;width:500px"><b>Cerified</b> Cleaning<br><b>Company</b></h2>
  <p class="lead" style="left:590px;top:964px;width:360px;font-size:13.5px;line-height:20.5px">Lorem ipsum dolor sit amet, consectetur adipiscing elit, sed do eiusmod tempor incididunt ut labore et dolore magna aliqua. Quis ipsum suspendisse ultrices gravida. Risus commodo viverra maecenas accumsan lacus vel facilisis.</p>
  <div class="btn" style="left:590px;top:1090px;width:112px;height:32px;font-size:13px">Read More</div>

  <!-- SERVICES -->
  <div class="eyebrow center" style="top:1208px">Our Services</div>
  <h2 class="h2 center" style="top:1222px">Feauted <b>Servies</b></h2>
  <p class="lead center" style="top:1277px">Lorem ipsum dolor sit amet, consectetur adipiscing elit, sed do eiusmod<br>tempor incididunt ut labore et dolore magna aliqua.</p>

  <div class="card" style="left:-195px;top:1400px;width:281px;height:327px">
    <div class="img" role="img" aria-label="Cleaner at work by a window" style="height:158px;background:linear-gradient(135deg,#9aa1a6,#d5d8da)"></div>
    <h3 style="font-size:20px;text-align:right;padding-right:250px;white-space:nowrap">Home owner sector</h3>
    <p style="font-size:12px;text-align:right">Lorem ipsum dolor sit amet, adipiscing elit, sed do tempor incididunt ut.</p>
  </div>
  <div class="card" style="left:134px;top:1361px;width:281px;height:405px">
    <div class="img" role="img" aria-label="Cleaner vacuuming next to a yellow sofa" style="background:linear-gradient(135deg,#f1f1f1,#d9d9d9 60%,#e8d36a)"></div>
    <h3>Home owner<br>sector</h3>
    <p>Lorem ipsum dolor sit amet, consectetur adipiscing elit, sed do eiusmod tempor incididunt ut.</p>
    <div class="more">Read More <svg width="20" height="10" viewBox="0 0 20 10"><path d="M0 5h18M14 1l4 4-4 4" stroke="currentColor" stroke-width="1.6" fill="none"/></svg></div>
  </div>
  <div class="card active" style="left:458px;top:1361px;width:283px;height:405px">
    <div class="img" role="img" aria-label="Two workers collecting litter in a park" style="background:linear-gradient(135deg,#6f8a5a,#a6b596 50%,#c5c0b4)"></div>
    <h3 style="margin-top:22px">Public sector</h3>
    <p>Lorem ipsum dolor sit amet, consectetur adipiscing elit, sed do eiusmod tempor incididunt ut.</p>
    <div class="more">Read More <svg width="20" height="10" viewBox="0 0 20 10"><path d="M0 5h18M14 1l4 4-4 4" stroke="currentColor" stroke-width="1.6" fill="none"/></svg></div>
  </div>
  <div class="card" style="left:785px;top:1361px;width:281px;height:405px">
    <div class="img" role="img" aria-label="Cleaners tidying a glass-walled meeting room" style="background:linear-gradient(135deg,#8c9296,#c8ccce 55%,#6e7478)"></div>
    <h3 style="margin-top:22px">Business sector</h3>
    <p>Lorem ipsum dolor sit amet, consectetur adipiscing elit, sed do eiusmod tempor incididunt ut.</p>
    <div class="more">Read More <svg width="20" height="10" viewBox="0 0 20 10"><path d="M0 5h18M14 1l4 4-4 4" stroke="currentColor" stroke-width="1.6" fill="none"/></svg></div>
  </div>
  <div class="card" style="left:1110px;top:1400px;width:281px;height:327px;text-align:left">
    <div class="img" role="img" aria-label="Cleaner vacuuming a living room" style="height:158px;background:linear-gradient(135deg,#cbb9a4,#e8e2da)"></div>
    <h3 style="font-size:20px;padding-left:64px">Corporate</h3>
    <p style="font-size:12px;margin-left:34px">Lorem ipsum dolor consectetur sed do eiusmod tempor</p>
  </div>
  <div class="dot" style="left:557px;top:1817px"></div>
  <div class="dot on" style="left:589px;top:1813px"></div>
  <div class="dot" style="left:629px;top:1817px"></div>

  <!-- STATS -->
  <div class="photo stats" role="img" aria-label="Dark close-up of a cleaning brush"></div>
  <div class="stat" style="left:143px"><strong>60+</strong><span>Trained Staff</span></div>
  <div class="stat" style="left:365px"><strong>04</strong><span>Branches</span></div>
  <div class="stat" style="left:590px"><strong>857</strong><span>Job Done</span></div>
  <div class="stat" style="left:824px"><strong>789</strong><span>Satified Clients</span></div>

  <!-- TEAM -->
  <div class="eyebrow center" style="top:2232px">Our Team</div>
  <h2 class="h2 center" style="top:2246px">Meet <b>Our Team</b></h2>
  <p class="lead center" style="top:2302px">Lorem ipsum dolor sit amet, consectetur adipiscing elit, sed do eiusmod<br>tempor incididunt ut labore et dolore magna aliqua.</p>

  <div class="member" style="left:215px;border:2px solid var(--green)">
    <div role="img" aria-label="Team member holding a basket of cleaning products" style="position:absolute;inset:0;background:linear-gradient(180deg,#ececec,#cfcfcf)"></div>
    <div class="tag"><b>Lorem Ipsum</b><small>Washer</small></div>
    <div class="soc"><i></i><i></i><i></i></div>
  </div>
  <div class="member" style="left:483px">
    <div role="img" aria-label="Team member in brown apron with arms crossed" style="position:absolute;inset:0;background:linear-gradient(180deg,#e4e4e4,#c4c4c4)"></div>
  </div>
  <div class="member" style="left:751px">
    <div role="img" aria-label="Team member holding a basket of cleaning supplies" style="position:absolute;inset:0;background:linear-gradient(180deg,#eeeeee,#d6d6d6)"></div>
  </div>

  <!-- TESTIMONIAL -->
  <div class="photo testi" role="img" aria-label="Faded office interior background"></div>
  <div class="eyebrow" style="left:183px;top:2836px">Testimonial</div>
  <h2 class="h2" style="left:183px;top:2856px;width:440px;line-height:44px"><b>Happy</b> Clients Say<br><b>About Company.</b></h2>
  <svg class="abs" style="left:210px;top:2970px" width="56" height="40" viewBox="0 0 56 40"><path d="M22 8c-8 0-14 6-14 14s6 14 14 14 M22 8c-8 4-12 10-12 18 M48 8c-8 0-14 6-14 14s6 14 14 14 M48 8c-8 4-12 10-12 18" stroke="var(--blue)" stroke-width="4" fill="none" stroke-linecap="round"/></svg>
  <p class="abs" style="left:210px;top:3020px;width:362px;font-size:13.5px;line-height:23px;font-style:italic;color:var(--muted)">Lorem ipsum dolor sit amet, consectetur adipiscing elit, sed do eiusmod tempor incididunt ut labore et dolore magna aliqua. Quis ipsum suspendisse ultrices gravida.</p>
  <div class="abs" style="left:210px;top:3127px;width:5px;height:40px;background:var(--green)"></div>
  <div class="abs" style="left:223px;top:3126px;font-size:18px;font-weight:500;color:var(--ink);line-height:22px">Lorem Ipsum<br><span style="font-size:12px;font-weight:400;color:var(--muted)">Washer</span></div>
  <div class="abs" style="left:703px;top:2803px;width:265px;height:316px;background:var(--green);border-radius:6px"></div>
  <div class="photo" role="img" aria-label="Businessman in a navy suit holding a tablet" style="left:614px;top:2819px;width:325px;height:329px;border-radius:10px;background:linear-gradient(135deg,#f2f2f2,#d8dadf 55%,#243b63);box-shadow:0 8px 22px rgba(0,0,0,.2)"></div>
  <div class="arrow-btn" style="left:55px;top:2946px"><svg width="10" height="12" viewBox="0 0 10 12"><path d="M7 1L2 6l5 5" stroke="#222" stroke-width="2" fill="none"/></svg></div>
  <div class="arrow-btn" style="left:1109px;top:2946px"><svg width="10" height="12" viewBox="0 0 10 12"><path d="M3 1l5 5-5 5" stroke="#222" stroke-width="2" fill="none"/></svg></div>

  <!-- BLOG -->
  <div class="eyebrow center" style="top:3305px">News &amp; Updated</div>
  <h2 class="h2 center" style="top:3320px"><b>Resent</b> Blog &amp; <b>News</b></h2>
  <p class="lead center" style="top:3375px">Lorem ipsum dolor sit amet, consectetur adipiscing elit,</p>

  <div class="post" style="left:146px">
    <div class="img" role="img" aria-label="Cleaner in blue uniform carrying a basket of supplies" style="background:linear-gradient(135deg,#2b3d66,#9aa3b2 55%,#e5c850)"><div class="date">02<hr>Feb</div></div>
    <h4>How to Clean<br>Appartment Area.</h4>
    <p>Lorem ipsum dolor sit amet, consectetur adipiscing elit, sed do eiusmod tempor incididunt ut.</p>
    <div class="meta"><i></i>By; Admin<svg style="margin-left:auto" width="20" height="10" viewBox="0 0 20 10"><path d="M0 5h18M14 1l4 4-4 4" stroke="#222" stroke-width="1.6" fill="none"/></svg></div>
  </div>
  <div class="post" style="left:459px">
    <div class="img" role="img" aria-label="Cleaners vacuuming and wiping in a living room" style="background:linear-gradient(135deg,#8f7d70,#d9d3cd 55%,#3a4a6b)"><div class="date">02<hr>Feb</div></div>
    <h4>How to Clean<br>Appartment Area.</h4>
    <p>Lorem ipsum dolor sit amet, consectetur adipiscing elit, sed do eiusmod tempor incididunt ut.</p>
    <div class="meta"><i></i>By; Admin<svg style="margin-left:auto" width="20" height="10" viewBox="0 0 20 10"><path d="M0 5h18M14 1l4 4-4 4" stroke="#222" stroke-width="1.6" fill="none"/></svg></div>
  </div>
  <div class="post" style="left:773px">
    <div class="img" role="img" aria-label="Team cleaning a bright apartment" style="background:linear-gradient(135deg,#d7cbbd,#f1ece6 55%,#46597e)"><div class="date">02<hr>Feb</div></div>
    <h4>How to Clean<br>Appartment Area.</h4>
    <p>Lorem ipsum dolor sit amet, consectetur adipiscing elit, sed do eiusmod tempor incididunt ut.</p>
    <div class="meta"><i></i>By; Admin<svg style="margin-left:auto" width="20" height="10" viewBox="0 0 20 10"><path d="M0 5h18M14 1l4 4-4 4" stroke="#222" stroke-width="1.6" fill="none"/></svg></div>
  </div>

  <!-- FOOTER -->
  <div class="photo footer" role="img" aria-label="Dark faded background of a cleaner at work"></div>
  <div class="abs newsletter"></div>
  <div class="abs" style="left:130px;top:3962px;font-size:26px;font-weight:600;color:var(--white)">Subscribe to Our Newsletter</div>
  <div class="abs" style="left:575px;top:3959px;width:430px;height:43px;background:var(--white);border-radius:22px;font-size:13px;color:#999;line-height:43px;padding-left:16px">Enter Your Email</div>
  <div class="abs" style="left:864px;top:3959px;width:141px;height:43px;border-radius:22px;background:linear-gradient(90deg,#1a8fd6,#2aa7ee);color:var(--white);font-size:16px;font-weight:500;display:flex;align-items:center;justify-content:center">Subscribe</div>

  <div class="logo" style="left:144px;top:4128px;font-size:30px;color:var(--white)"><i style="width:48px;height:48px;margin-right:4px"></i>TKR Clean AB</div>
  <p class="abs" style="left:144px;top:4183px;width:270px;font-size:11px;line-height:17px;color:#cfcfcf">Lorem ipsum dolor sit amet, consectetur adipiscing elit, sed do eiusmod tempor incididunt ut labore et dolore magna aliqua.</p>
  <div class="abs" style="left:144px;top:4248px;width:195px;height:1px;background:#555"></div>
  <div class="abs" style="left:146px;top:4271px;display:flex;gap:30px">
    <i style="width:16px;height:16px;border-radius:50%;background:var(--white);display:block"></i>
    <i style="width:16px;height:16px;border-radius:50%;background:var(--white);display:block"></i>
    <i style="width:16px;height:16px;border-radius:50%;background:var(--white);display:block"></i>
    <i style="width:16px;height:16px;border-radius:50%;background:var(--white);display:block"></i>
  </div>

  <div class="fcol" style="left:553px;top:4126px">
    <ul><li style="font-size:16px;margin-bottom:6px">Home</li><li>About us</li><li>Services</li><li>Pricing</li><li>Blog</li></ul>
  </div>
  <div class="fcol" style="left:720px;top:4126px">
    <ul><li style="font-size:16px;margin-bottom:6px">Contact Us</li><li>About us</li><li>Testimonial</li><li>Pricing</li><li>Faqs</li></ul>
  </div>
  <div class="fcol" style="left:914px;top:4126px">
    <h5 style="margin-bottom:8px">Call us Now</h5>
    <div style="font-size:13px;margin-bottom:10px">08-555 123 45</div>
    <div style="display:flex;align-items:center;gap:8px;font-size:11px"><svg width="16" height="11" viewBox="0 0 16 11"><rect x="0.5" y="0.5" width="15" height="10" fill="none" stroke="#fff"/><path d="M1 1l7 5 7-5" stroke="#fff" fill="none"/></svg>Email us</div>
    <div style="font-size:11px;margin:4px 0 14px">kontakt@tkrclean.se</div>
    <div style="display:flex;align-items:center;gap:8px;font-size:11px"><svg width="14" height="16" viewBox="0 0 14 16"><circle cx="7" cy="5" r="4" fill="none" stroke="#fff" stroke-width="1.5"/><path d="M1 15c1-4 11-4 12 0" stroke="#fff" stroke-width="1.5" fill="none"/></svg>Location</div>
    <div style="font-size:11px;margin-top:4px">kontakt@tkrclean.se</div>
  </div>

  <div class="abs" style="left:92px;top:4315px;width:1016px;height:1px;background:#444"></div>
  <div class="abs center" style="top:4332px;font-size:11px;color:#aaa">© Copyright 2022 TKR Clean AB &nbsp;| Org.nr: 556123-4567</div>
</div>
</body>
</html>
```